Harbor Bug Guard Business Cards

A modern business card with a predominantly white background and a sleek design featuring Harbor with complimentary greys or blacks to convey a professional and contemporary look.

Front:
Primarily white background. Limited use of company purple color can be neighbored by greys.
Text: Name, Title, Cell Phone, Office Phone, Website, email address

Back:
Background Continuation: The back of the card maintains the white background for consistency.
Company name “Harbor” in company color and font, “Bug Guard” underneath or underneath left justified of “Harbor.”
A subtle pattern or texture in shades of grey to add depth behind the company Logo in font.

logo color: hex #6212ab
font: antique olive nord D Regular

```html
<!DOCTYPE html>
<html lang="en">
<head>
<meta charset="utf-8">
<title>Harbor Bug Guard – Business Card</title>
<link href="https://fonts.googleapis.com/css2?family=Ubuntu:wght@400;700&display=swap" rel="stylesheet">
<style>
  :root {
    --brand: #6212ab;
    --ink: #555555;
    --ink-soft: #6f6f6f;
    --card: #fbfbfb;
    --band: #9a9a9a;
    --rule: #4f4f4f;
    --backdrop: #e9e7e4;
  }
  * { margin: 0; padding: 0; box-sizing: border-box; }
  html, body {
    width: 1200px;
    height: 1054px;
    overflow: hidden;
    background: var(--backdrop);
    font-family: "Ubuntu", sans-serif;
  }
  .business-card {
    position: absolute;
    left: 100px;
    top: 224px;
    width: 1000px;
    height: 605px;
    background: var(--card);
    border-radius: 26px;
    overflow: hidden;
    box-shadow: 0 10px 30px rgba(0,0,0,0.12);
  }
  .side-band {
    position: absolute;
    left: 0; top: 0;
    width: 99px; height: 100%;
    background: var(--band);
  }
  .side-rule {
    position: absolute;
    left: 101px; top: 0;
    width: 7px; height: 100%;
    background: var(--rule);
  }
  .wordmark {
    position: absolute;
    left: 148px;
    top: 62px;
    color: var(--brand);
    font-weight: 700;
  }
  .wordmark-primary {
    display: block;
    font-size: 78px;
    line-height: 1;
    letter-spacing: 3px;
  }
  .wordmark-secondary {
    display: block;
    font-size: 25px;
    line-height: 1;
    letter-spacing: 18.5px;
    margin-top: 4px;
  }
  .holder {
    position: absolute;
    left: 148px;
    top: 380px;
  }
  .holder-name {
    color: var(--brand);
    font-weight: 700;
    font-size: 40px;
    line-height: 1.1;
  }
  .holder-title {
    color: var(--ink-soft);
    font-size: 23px;
    margin-top: 6px;
  }
  .contact-list {
    position: absolute;
    left: 148px;
    top: 486px;
    display: grid;
    grid-template-columns: 320px auto;
    row-gap: 10px;
    list-style: none;
  }
  .contact-item {
    display: flex;
    align-items: center;
    gap: 18px;
    color: var(--ink);
    font-size: 23px;
    height: 30px;
  }
  .contact-icon {
    width: 22px;
    height: 22px;
    fill: var(--brand);
    flex: none;
  }
</style>
</head>
<body>
  <main class="business-card">
    <div class="side-band"></div>
    <div class="side-rule"></div>

    <div class="wordmark">
      <span class="wordmark-primary">HARBOR</span>
      <span class="wordmark-secondary">BUG GUARD</span>
    </div>

    <div class="holder">
      <h1 class="holder-name">Daniel Reyes</h1>
      <p class="holder-title">Managing Director</p>
    </div>

    <ul class="contact-list">
      <li class="contact-item">
        <svg class="contact-icon" viewBox="0 0 24 24" aria-hidden="true"><path d="M6.6 10.8c1.4 2.8 3.8 5.1 6.6 6.6l2.2-2.2c.3-.3.7-.4 1-.2 1.1.4 2.3.6 3.6.6.6 0 1 .4 1 1V20c0 .6-.4 1-1 1C10.6 21 3 13.4 3 4c0-.6.4-1 1-1h3.5c.6 0 1 .4 1 1 0 1.3.2 2.5.6 3.6.1.3 0 .7-.2 1z"/></svg>
        <span>000-0000-0000</span>
      </li>
      <li class="contact-item">
        <svg class="contact-icon" viewBox="0 0 24 24" aria-hidden="true"><path d="M2 4h20v5h-5V7H7v2H2z"/><rect x="2" y="6" width="20" height="0"/><path d="M5 12l2-3h10l2 3v8H5z"/></svg>
        <span>name@harborbugguard.com</span>
      </li>
      <li class="contact-item">
        <svg class="contact-icon" viewBox="0 0 24 24" aria-hidden="true"><path d="M2 5h20v14H2z M3.5 6.5l8.5 6.5 8.5-6.5" fill="var(--brand)"/><path d="M3.5 6.5l8.5 6.5 8.5-6.5" fill="none" stroke="#fbfbfb" stroke-width="1.5"/></svg>
        <span>099-0999-0999</span>
      </li>
      <li class="contact-item">
        <svg class="contact-icon" viewBox="0 0 24 24" aria-hidden="true"><circle cx="12" cy="12" r="10"/><path d="M2 12h20M12 2c3 3 3 17 0 20M12 2c-3 3-3 17 0 20" fill="none" stroke="#fbfbfb" stroke-width="1.4"/></svg>
        <span>www.harborbugguard.com</span>
      </li>
    </ul>
  </main>
</body>
</html>
```